Post Card Mailer for QUIK PATH PROSPECTS using new logo

We need a post card designed to send through the USA mail service that will go to new prospective clients.

The post card will introduce me and my new company and try to educate them our on company and services.

The goal is for them to call me or email me so I can have a discussion and try to sell our product.

Our product is a name list of individuals that are looking for consulting / help to determine if they qualify for USA social security benefits and then help to manage the process. We sell this name list to law firms that help these individuals.

Our services are better because we have a better less expensive way to identify people via the internet that want help. Our conversion rate is 15%, so every 100 leads a law firm buys the will obtain 15 customers / clients.
Updates

Designer on Logo took alot longer than expected. Also there were two projects that needed to combined into one. Which was done yesterday.

Went on vacation/holiday

Target Market(s)

Law firms

Font styles to use
Serif
Sans Serif
Script

Colors

Designer to choose colors to be used in the design.

Requirements
Must have
• The size of the mailer should be about 6 by 8 inches.
• Two sides.
• Side 1: With our Logo and key messages we want to communicate.
• Side 2: A space to be used by the USA mail services in lower right, my photo and an introduction by me to our company and why they should buy from my company.
Nice to have
• Images that represent what we do, how we help, and our target market.
Should not have
• Poor taste in images that upset people

```html
<!DOCTYPE html>
<html lang="en">
<head>
<meta charset="utf-8">
<title>QUIK PATH PROSPECTS – Postcard Mailer</title>
<link href="https://fonts.googleapis.com/css2?family=Roboto+Condensed:ital,wght@0,300;0,400;0,500;0,700;1,300;1,400&family=Roboto:wght@400;700&display=swap" rel="stylesheet">
<style>
  :root {
    --page: #f6f6f6;
    --navy-deep: #0a1529;
    --navy: #142b52;
    --band: #2f5ea8;
    --accent: #2d5db0;
    --ink: #1c1c1c;
    --white: #ffffff;
    --frame: #4a4a4a;
  }
  * { box-sizing: border-box; margin: 0; padding: 0; }
  html, body { width: 814px; height: 1200px; overflow: hidden; }
  body {
    background: var(--page);
    position: relative;
    font-family: "Roboto Condensed", "Arial Narrow", sans-serif;
    color: var(--white);
  }
  .card {
    position: absolute;
    left: 49px;
    width: 719px;
    background: var(--white);
    overflow: hidden;
  }
  .card-front { top: 43px; height: 539px; }
  .card-back { top: 618px; height: 540px; }
  .band { position: absolute; left: 0; right: 0; background: var(--band); }

  /* Front */
  .front-top-band { top: 0; height: 12px; }
  .front-scene {
    position: absolute; top: 12px; left: 0; right: 0; height: 307px;
    background: linear-gradient(100deg, #2a2c30 0%, #5b6068 30%, #9aa6ae 55%, #c9d3d6 75%, #6f7884 100%);
  }
  .front-logo {
    position: absolute; top: 122px; left: 0; right: 0;
    text-align: center;
    font-weight: 700; font-size: 46px; letter-spacing: 1px;
    color: var(--white);
  }
  .front-panel {
    position: absolute; top: 319px; left: 0; right: 0; height: 206px;
    background: linear-gradient(90deg, var(--navy-deep) 0%, var(--navy) 100%);
  }
  .front-bottom-band { top: 525px; height: 14px; }
  .feature { position: absolute; }
  .feature-icon { position: absolute; }
  .feature-title { font-size: 18px; font-weight: 500; line-height: 22px; }
  .feature-list { list-style: none; font-size: 15px; font-weight: 500; line-height: 18px; }
  .feature-list li::before { content: "\2022\00a0"; }

  /* Back */
  .back-top-band { top: 0; height: 14px; }
  .back-header {
    position: absolute; top: 14px; left: 0; right: 0; height: 225px;
    background: linear-gradient(90deg, #05080f 0%, var(--navy-deep) 35%, var(--navy) 100%);
  }
  .portrait {
    position: absolute; left: 59px; top: 15px; width: 128px; height: 161px;
    background: linear-gradient(180deg, #c9c9c9 0%, #a7a7a7 55%, #2b2e35 100%);
  }
  .portrait-caption {
    position: absolute; left: 65px; top: 184px;
    font-style: italic; font-size: 13px; line-height: 16px;
  }
  .back-logo {
    position: absolute; left: 290px; width: 340px; top: 62px;
    text-align: center; font-weight: 700; font-size: 30px; letter-spacing: 1px;
  }
  .back-tagline {
    position: absolute; left: 220px; right: 0; top: 150px;
    text-align: center; font-weight: 700; font-size: 19px;
  }
  .back-subline {
    position: absolute; left: 240px; right: 0; top: 175px;
    text-align: center; font-style: italic; font-weight: 300; font-size: 17px;
  }
  .intro {
    position: absolute; left: 30px; width: 327px; top: 254px; color: var(--ink);
  }
  .intro-heading { color: var(--accent); font-size: 14px; font-weight: 500; margin-bottom: 10px; }
  .intro-list { list-style: none; font-family: "Roboto", Arial, sans-serif; font-size: 9.4px; line-height: 12px; text-align: justify; }
  .intro-list li { margin-bottom: 2.5px; }
  .intro-list li::before { content: "\2022\00a0\00a0"; }
  .intro-close { color: var(--accent); font-size: 14px; font-weight: 500; line-height: 17px; margin-top: 16px; }
  .contact-band {
    position: absolute; left: 0; width: 339px; top: 478px; height: 62px;
    background: var(--band);
  }
  .contact-label { position: absolute; left: 30px; top: 7px; font-size: 19px; font-weight: 700; }
  .contact-line {
    position: absolute; left: 30px; top: 34px; font-size: 14px; font-weight: 700;
    display: flex; align-items: center; gap: 6px; white-space: nowrap;
  }
  .contact-line svg { flex: none; }
  .contact-email { margin-left: 18px; display: flex; align-items: center; gap: 6px; }
  .offer {
    position: absolute; left: 339px; right: 0; top: 252px; height: 76px;
    background: var(--band); border-radius: 38px 0 0 38px;
  }
  .offer-title {
    position: absolute; left: 18px; width: 100px; top: 15px;
    text-align: center; font-size: 22px; font-weight: 500; line-height: 23px;
  }
  .offer-list {
    position: absolute; left: 132px; top: 10px; list-style: none;
    font-size: 14px; font-weight: 500; line-height: 19px;
  }
  .offer-list li::before { content: "\2022\00a0"; }
  .mail-area {
    position: absolute; left: 340px; width: 359px; top: 346px; height: 180px;
    border: 1px solid var(--frame); background: var(--white); color: var(--ink);
  }
  .return-address {
    position: absolute; left: 12px; top: 10px;
    font-family: "Roboto", Arial, sans-serif; font-size: 7.6px; line-height: 9.4px;
  }
  .return-address strong { font-weight: 700; }
  .postage {
    position: absolute; right: 11px; top: 10px; width: 50px; height: 63px;
    border: 1px solid var(--frame);
    display: flex; align-items: center; justify-content: center;
    font-family: "Roboto", Arial, sans-serif; font-size: 7.5px;
  }
</style>
</head>
<body>

<section class="card card-front">
  <div class="band front-top-band"></div>
  <div class="front-scene" role="img" aria-label="Photo of a professional at a laptop showing charts, meeting across a desk"></div>
  <div class="front-logo">QUIK PATH PROSPECTS</div>

  <div class="front-panel">
    <div class="feature" style="left:33px; top:30px;">
      <svg class="feature-icon" style="left:0; top:12px;" width="58" height="38" viewBox="0 0 58 38" aria-hidden="true">
        <path d="M2 8 L14 4 L22 22 L10 28 Z M56 8 L44 4 L36 22 L48 28 Z" fill="#fff"/>
        <path d="M16 8 Q26 2 34 8 L40 20 Q36 30 28 34 Q20 34 14 26" fill="none" stroke="#fff" stroke-width="3" stroke-linejoin="round"/>
        <path d="M22 24 L26 28 M26 20 L31 25 M30 16 L35 21" stroke="#fff" stroke-width="2.4" stroke-linecap="round"/>
      </svg>
    </div>
    <div class="feature" style="left:106px; top:26px; width:260px;">
      <h3 class="feature-title">Best Leads, Best Price</h3>
      <ul class="feature-list">
        <li>Our high conversion rates lower your client acquisition cost</li>
        <li>Referrals available</li>
      </ul>
    </div>

    <div class="feature" style="left:41px; top:118px;">
      <svg class="feature-icon" style="left:0; top:0;" width="42" height="46" viewBox="0 0 42 46" aria-hidden="true">
        <path d="M21 3 L38 9 V22 Q38 36 21 43 Q4 36 4 22 V9 Z" fill="none" stroke="#fff" stroke-width="3.4" stroke-linejoin="round"/>
        <path d="M13 23 L19 29 L30 17" fill="none" stroke="#fff" stroke-width="3.4" stroke-linecap="round" stroke-linejoin="round"/>
      </svg>
    </div>
    <div class="feature" style="left:106px; top:117px; width:260px;">
      <h3 class="feature-title">Trusted Partner</h3>
      <ul class="feature-list">
        <li>Reliability, Dependable, Helpful</li>
        <li>Deep business &amp; process acumen</li>
      </ul>
    </div>

    <div class="feature" style="left:391px; top:26px;">
      <svg class="feature-icon" style="left:0; top:0;" width="52" height="54" viewBox="0 0 52 54" aria-hidden="true">
        <rect x="2" y="38" width="11" height="8" fill="#fff"/>
        <rect x="16" y="30" width="11" height="16" fill="#fff"/>
        <rect x="30" y="18" width="11" height="28" fill="#fff"/>
        <path d="M35.5 0 L46 12 H40 V26 H31 V12 H25 Z" fill="#fff"/>
        <rect x="0" y="49" width="50" height="3" fill="#fff"/>
      </svg>
    </div>
    <div class="feature" style="left:461px; top:26px; width:250px;">
      <h3 class="feature-title">High Volume, Quality Leads</h3>
      <ul class="feature-list">
        <li>50 years of SSD domain knowledge</li>
        <li>Tested technology capabilities</li>
      </ul>
    </div>

    <div class="feature" style="left:385px; top:108px;">
      <svg class="feature-icon" style="left:0; top:0;" width="62" height="46" viewBox="0 0 62 46" aria-hidden="true">
        <rect x="9" y="4" width="44" height="30" rx="2" fill="none" stroke="#fff" stroke-width="3"/>
        <path d="M2 38 H60 L56 44 H6 Z" fill="#fff"/>
        <rect x="17" y="22" width="3" height="6" fill="#fff"/>
        <rect x="22" y="18" width="3" height="10" fill="#fff"/>
        <rect x="27" y="20" width="3" height="8" fill="#fff"/>
        <rect x="32" y="13" width="3" height="15" fill="#fff"/>
        <rect x="37" y="16" width="3" height="12" fill="#fff"/>
        <rect x="42" y="10" width="3" height="18" fill="#fff"/>
        <rect x="15" y="29" width="32" height="1.6" fill="#fff"/>
      </svg>
    </div>
    <div class="feature" style="left:461px; top:101px; width:250px;">
      <h3 class="feature-title">Easy to use</h3>
      <ul class="feature-list">
        <li>Integrate seamlessly<br>into your IT systems</li>
      </ul>
    </div>
  </div>
  <div class="band front-bottom-band"></div>
</section>

<section class="card card-back">
  <div class="band back-top-band"></div>
  <header class="back-header">
    <div class="portrait" role="img" aria-label="Portrait photo of Marcus Delaney, company president"></div>
    <p class="portrait-caption">Marcus Delaney<br>President, QUIK PATH PROSPECTS</p>
    <div class="back-logo">QUIK PATH PROSPECTS</div>
    <p class="back-tagline">Best Leads... Best Price with High Volume &amp; Quality capacity...</p>
    <p class="back-subline">Leads from a Trusted Partner that is Easy to use</p>
  </header>

  <div class="intro">
    <h2 class="intro-heading">I want to personally introduce our company to you!</h2>
    <ul class="intro-list">
      <li>My team as &gt; 50 years of cumulative SSD experience.</li>
      <li>We have proven technology that delivers the best leads.</li>
      <li>The timing is right for a new competitor in this industry.</li>
      <li>I had to come out of retirement after 30 years with a Fortune 500 firm, the opportunity is just that great... I love building businesses and partnering with great customers!</li>
      <li>Our business, industry, &amp; technical acumen is unrivaled... and we can do it at a cost than no others can.</li>
    </ul>
    <p class="intro-close">Let's work together to bring Social Security Disability benefits to those in need and deserving!</p>
  </div>

  <div class="contact-band">
    <p class="contact-label">Contact:</p>
    <p class="contact-line">
      <svg width="14" height="16" viewBox="0 0 14 16" aria-hidden="true"><path d="M3 1 L6 5 L4.5 7 Q6 11 9 12.5 L11 11 L13.5 14 L11.5 15.5 Q3 14 1 3 Z" fill="#fff"/></svg>
      <span>555-014-2278</span>
      <span class="contact-email">
        <svg width="20" height="14" viewBox="0 0 20 14" aria-hidden="true"><rect x="1" y="1" width="18" height="12" fill="none" stroke="#fff" stroke-width="1.6"/><path d="M1 1 L10 8 L19 1" fill="none" stroke="#fff" stroke-width="1.6"/></svg>
        <span>marcus@quikpath.com</span>
      </span>
    </p>
  </div>

  <div class="offer">
    <p class="offer-title">Test our Leads!</p>
    <ul class="offer-list">
      <li>Start at 250 or 500 Leads.</li>
      <li>Grow to 1,000 ... 3,000 or even 10,000!</li>
      <li>We give the right support to your growth.</li>
    </ul>
  </div>

  <div class="mail-area">
    <p class="return-address">
      <strong>Marcus Delaney, President QUIK PATH PROSPECTS</strong><br>
      1250 Harbor Street, Suite 300<br>
      Columbus OH 43215<br>
      555-014-2278<br>
      marcus@quikpath.com
    </p>
    <div class="postage">POSTAGE</div>
  </div>
</section>

</body>
</html>
```